VONTRAQUEL.COM - AIUTOMATED SALES

After the succesfully created logo for our new startup, we want to have a wordpress design according to the logo and the colours.

The company focussing on sales with AI based conversations. Focussing on social media. Furthermore it will offer whitelabeled AI - UTOMATED sales activities based on ChatGPT and Bard.

Target Market(s)

Tech companies / Mid market IT staff

Coding

Coded - Design and coding required

Requirements
Must have
• AI pictures

```html
<!DOCTYPE html>
<html lang="en">
<head>
<meta charset="utf-8">
<title>Vontraquel – AIutomated Sales</title>
<link rel="stylesheet" href="https://fonts.googleapis.com/css2?family=Lexend:wght@400;500;600&family=Inter:wght@400;500;600;700&display=swap">
<style>
:root{
  --night:#020b16;
  --navy:#083459;
  --footer:#063359;
  --teal:#4795a8;
  --ink:#1d1d1f;
  --muted:#555b63;
  --card:#edf4fb;
  --sky:#a3c3de;
  --white:#ffffff;
  --link:#2a7fa0;
}
*{box-sizing:border-box;margin:0;padding:0}
html,body{width:1200px;height:4655px;overflow:hidden}
body{font-family:"Inter",sans-serif;color:var(--ink);background:var(--white)}
section,footer{position:relative;width:1200px;overflow:hidden}
.abs{position:absolute}
h1,h2,.price,.tab{font-family:"Lexend",sans-serif;font-weight:500}
.btn{position:absolute;display:flex;align-items:center;justify-content:center;background:var(--teal);color:var(--white);font-weight:600;font-size:11px;text-decoration:none}
.body-text{font-size:12px;line-height:21px;color:var(--muted)}
.body-text p+p{margin-top:21px}

/* hero */
.hero{height:750px;background:var(--night);color:var(--white)}
.hero-visual{left:0;right:0;top:390px;height:360px;background:radial-gradient(ellipse 70% 45% at 50% 35%,#8a5a78 0%,#3d2a44 35%,transparent 70%),linear-gradient(180deg,var(--night),#1a1522 60%,#2a1f2c)}
.brand{display:flex;align-items:center;gap:8px;font-family:"Inter",sans-serif;font-weight:600;color:var(--white);letter-spacing:1px}
.brand .dot{width:22px;height:22px;border:2px solid var(--white);border-radius:50%}
.hero .brand{left:127px;top:56px;font-size:16px}
.main-nav{left:480px;top:60px;width:595px;display:flex;justify-content:space-between;font-size:11px}
.main-nav a,.foot-nav a{color:inherit;text-decoration:none}
.hero h1{left:0;width:1200px;top:228px;text-align:center;font-size:47px;line-height:57px}
.hero .lead{left:320px;width:560px;top:368px;text-align:center;font-size:11px;line-height:19px;color:#d5dbe3}
.hero .btn{left:493px;top:459px;width:212px;height:43px}

/* sales personal */
.sales{height:706px;background:var(--white)}
.network{right:0;top:0;width:620px;height:706px;background:radial-gradient(circle at 75% 40%,#bfe7fb 0%,#e6f6fd 45%,transparent 75%)}
.sales h2{left:125px;top:150px;font-size:40px}
.sales .body-text{left:125px;top:228px;width:394px}
.sales .btn{left:125px;top:491px;width:213px;height:44px}

/* social */
.social{height:611px;background:linear-gradient(90deg,#f4f4f4,#e4e4e6)}
.robot{left:0;top:0;width:650px;height:611px;background:radial-gradient(ellipse 45% 60% at 45% 55%,#c9ccd2,#e8e8ea 70%)}
.social h2{left:683px;top:118px;width:420px;font-size:40px;line-height:55px}
.social .body-text{left:683px;top:235px;width:395px}

/* pricing */
.pricing{height:1117px;background:var(--white)}
.pricing h2{left:125px;top:100px;font-size:36px}
.pricing .intro{left:125px;top:159px;width:680px;font-size:11px;line-height:21px;color:var(--muted)}
.plan{left:125px;width:950px;height:365px;background:var(--card)}
.tab{position:absolute;left:-13px;top:27px;width:430px;height:55px;background:var(--navy);color:var(--white);font-size:26px;display:flex;align-items:center;justify-content:center}
.tab::after{content:"";position:absolute;left:0;bottom:-12px;border-left:13px solid transparent;border-top:12px solid var(--navy);filter:brightness(.7)}
.plan .desc{position:absolute;left:79px;top:123px;width:720px;font-size:16px;line-height:28px;color:#3d4550}
.price{position:absolute;left:79px;top:192px;font-size:42px;color:var(--navy);font-weight:600}
.plan .btn{left:79px;top:257px;width:353px;height:56px;font-size:18px;letter-spacing:1px}

/* statement */
.statement{height:710px;background:var(--sky)}
.hand{left:650px;top:150px;width:550px;height:480px;background:radial-gradient(ellipse 55% 40% at 60% 45%,#f2f4f8,#c4d6e8 60%,transparent 85%)}
.statement h2{left:152px;top:100px;font-size:36px}
.statement .intro{left:152px;top:159px;width:462px;font-size:12px;line-height:22px;color:#2f3d4d}
.quote{left:152px;width:462px;height:146px;background:var(--white);padding:28px 36px}
.quote h3{font-size:14px;font-weight:600;color:var(--navy);margin-bottom:10px}
.quote p{font-size:11px;line-height:19px;color:var(--muted)}
.quote span{display:block;margin-top:12px;font-size:10px;font-weight:600;color:var(--link)}

/* philosophy */
.philosophy{height:483px;background:var(--white)}
.philosophy h2{left:0;width:1200px;top:100px;text-align:center;font-size:36px}
.philosophy .body-text{left:280px;width:640px;top:163px;text-align:center;font-size:11px;line-height:21px}
.philosophy .btn{left:493px;top:340px;width:213px;height:43px}

/* footer */
.site-footer{height:278px;background:var(--footer);color:var(--white)}
.site-footer .brand{left:121px;top:120px;font-size:24px;flex-direction:column;gap:10px}
.site-footer .brand .dot{width:54px;height:54px}
.foot-nav{left:493px;top:105px;width:582px;display:flex;justify-content:space-between;font-size:13px}
.copyright{right:125px;top:158px;font-size:13px}
</style>
</head>
<body>

<section class="hero">
  <div class="abs hero-visual" role="img" aria-label="Glowing pink and white digital particle network wave"></div>
  <div class="abs brand"><span class="dot"></span>VONTRAQUEL</div>
  <nav class="abs main-nav">
    <a href="#sales">Sales Personal</a><a href="#social">AIUTOMATED Social Media</a><a href="#pricing">Pricing</a><a href="#statement">Statement</a><a href="#philosophy">Philosophy</a>
  </nav>
  <h1 class="abs">Where AI Meets<br>Conversations For Success</h1>
  <p class="abs lead">Lorem Ipsum is simply dummy text of the printing and typesetting industry. Lorem Ipsum has been the industry's standard dummy text ever since the 1500s, when an unknown printer took a galley of type and scrambled it to make a type specimen book.</p>
  <a class="btn" href="#pricing">Automate All Prospecting</a>
</section>

<section class="sales" id="sales">
  <div class="abs network" role="img" aria-label="Light blue connected node network graphic"></div>
  <h2 class="abs">Sales Personal</h2>
  <div class="abs body-text">
    <p>Lorem Ipsum is simply dummy text of the printing and typesetting industry. Lorem Ipsum has been the industry's standard dummy text ever since the 1500s, when an unknown printer took a galley of type and scrambled it to make a type specimen book. It has survived not only five centuries, but also the leap into electronic typesetting, remaining essentially unchanged.</p>
    <p>It was popularised in the 1960s with the release of Pressmark sheets containing Lorem Ipsum passages, and more recently with desktop publishing software like Layoutwise including versions of Lorem Ipsum.</p>
  </div>
  <a class="btn" href="#">Click For Learn More</a>
</section>

<section class="social" id="social">
  <div class="abs robot" role="img" aria-label="White humanoid robot dissolving into pixels, thinking pose"></div>
  <h2 class="abs">AIUTOMATED Social Media</h2>
  <div class="abs body-text">
    <p>Lorem Ipsum is simply dummy text of the printing and typesetting industry. Lorem Ipsum has been the industry's standard dummy text ever since the 1500s, when an unknown printer took a galley of type and scrambled it to make a type specimen book. It has survived not only five centuries, but also the leap into electronic typesetting, remaining essentially unchanged.</p>
    <p>It was popularised in the 1960s with the release of Pressmark sheets containing Lorem Ipsum passages, and more recently with desktop publishing software like Layoutwise including versions of Lorem Ipsum.</p>
  </div>
</section>

<section class="pricing" id="pricing">
  <h2 class="abs">Pricing</h2>
  <p class="abs intro">It was popularised in the 1960s with the release of Pressmark sheets containing Lorem Ipsum passages, and more recently with desktop publishing software like Layoutwise including versions of Lorem Ipsum.</p>
  <div class="abs plan" style="top:260px">
    <div class="tab">STARTER</div>
    <p class="desc">Lorem Ipsum is simply dummy text of the printing and typesetting industry. Lorem Ipsum has been the industry's standard dummy text ever since the 1500s,</p>
    <div class="price">$ 14.39</div>
    <a class="btn" href="#">START FREE TRIAL</a>
  </div>
  <div class="abs plan" style="top:651px">
    <div class="tab">PRO</div>
    <p class="desc">Lorem Ipsum is simply dummy text of the printing and typesetting industry. Lorem Ipsum has been the industry's standard dummy text ever since the 1500s,</p>
    <div class="price" style="left:74px">$ 44.99</div>
    <a class="btn" href="#">JOIN</a>
  </div>
</section>

<section class="statement" id="statement">
  <div class="abs hand" role="img" aria-label="White robotic hand reaching toward a glowing AI chip icon"></div>
  <h2 class="abs">Statement</h2>
  <p class="abs intro">It was popularised in the 1960s with the release of Pressmark sheets containing Lorem Ipsum passages, and more recently with desktop publishing software like Layoutwise including versions of Lorem Ipsum.</p>
  <div class="abs quote" style="top:291px">
    <h3>Marlo Fenwick</h3>
    <p>Lorem Ipsum is simply dummy text of the printing and typesetting industry. Lorem Ipsum has been the industry's standard.</p>
    <span>LOREM IPSUM</span>
  </div>
  <div class="abs quote" style="top:453px">
    <h3>Marlo Fenwick</h3>
    <p>Lorem Ipsum is simply dummy text of the printing and typesetting industry. Lorem Ipsum has been the industry's standard.</p>
    <span>LOREM IPSUM</span>
  </div>
</section>

<section class="philosophy" id="philosophy">
  <h2 class="abs">Philosophy</h2>
  <div class="abs body-text">
    <p>Lorem Ipsum is simply dummy text of the printing and typesetting industry. Lorem Ipsum has been the industry's standard dummy text ever since the 1500s, when an unknown printer took a galley of type and scrambled it to make a type specimen book. It has survived not only five centuries, but also the leap into electronic typesetting, remaining essentially unchanged.</p>
    <p>It was popularised in the 1960s with the release of Pressmark sheets containing Lorem Ipsum passages, and more recently with desktop publishing software like Layoutwise including versions of Lorem Ipsum.</p>
  </div>
  <a class="btn" href="#">Click For Learn More</a>
</section>

<footer class="site-footer">
  <div class="abs brand"><span class="dot"></span>VONTRAQUEL</div>
  <nav class="abs foot-nav">
    <a href="#sales">Sales Personal</a><a href="#social">AIUTOMATED Social Media</a><a href="#pricing">Pricing</a><a href="#statement">Statement</a><a href="#philosophy">Philosophy</a>
  </nav>
  <p class="abs copyright">Copyright@2023-Vontraquel</p>
</footer>

</body>
</html>
```